First Aid Training business needs business card design

We would like a double sided business card designed for a first aid training business - Brindlewood First Aid. We provide first aid training and , WHS (work, health and safety) training.

The attached word document contains the key information we would like on each side of the business card.

Final design needs to be delivered in print ready format, along with the original file.

```html
<!DOCTYPE html>
<html lang="en">
<head>
<meta charset="UTF-8">
<title>Brindlewood First Aid – Business Card</title>
<link href="https://fonts.googleapis.com/css2?family=Montserrat:wght@500;600;700&display=swap" rel="stylesheet">
<style>
  :root {
    --red: #ec1f24;
    --grey: #838383;
    --ink: #111111;
    --paper: #ffffff;
    --backdrop: #8a8a8a;
    --rule: #9a9a9a;
  }
  * { box-sizing: border-box; margin: 0; padding: 0; }
  html, body { width: 1200px; height: 1017px; overflow: hidden; }
  body {
    background: var(--backdrop);
    font-family: "Montserrat", sans-serif;
    position: relative;
  }
  .card {
    position: absolute;
    width: 620px;
    height: 378px;
    background: var(--paper);
    overflow: hidden;
    box-shadow: 0 10px 30px rgba(0,0,0,0.25);
  }
  /* front */
  .card-front { left: 60px; top: 90px; }
  .brand {
    position: absolute;
    left: 40px;
    top: 120px;
    width: 250px;
  }
  .brand-dot {
    width: 90px; height: 90px;
    border-radius: 50%;
    background: var(--red);
    margin-bottom: 18px;
  }
  .brand-name {
    color: var(--ink);
    font-weight: 700;
    font-size: 27px;
    line-height: 1.15;
    text-transform: uppercase;
    letter-spacing: 0.5px;
  }
  .pitch {
    position: absolute;
    left: 330px;
    top: 56px;
    width: 260px;
  }
  .pitch-title {
    color: var(--red);
    font-weight: 700;
    font-size: 20px;
    line-height: 1.1;
  }
  .pitch-sub {
    color: var(--grey);
    font-weight: 700;
    font-size: 20px;
    line-height: 1.2;
  }
  .pitch-rule {
    position: relative;
    height: 1px;
    background: var(--rule);
    margin: 8px 0 16px;
  }
  .pitch-rule::before {
    content: "";
    position: absolute;
    left: 0; top: -2px;
    width: 64px; height: 4px;
    background: var(--red);
  }
  .benefits, .services { list-style: none; }
  .benefits li, .services li {
    position: relative;
    padding-left: 24px;
    margin-bottom: 8px;
  }
  .benefits li {
    color: var(--ink);
    font-weight: 600;
    font-size: 14px;
    line-height: 1.25;
  }
  .benefits li::before, .services li::before {
    content: "+";
    position: absolute;
    left: 2px; top: -1px;
    color: var(--red);
    font-weight: 700;
  }
  .services { margin-top: 26px; }
  .services li {
    color: var(--grey);
    font-weight: 600;
    font-size: 15px;
    text-transform: uppercase;
    margin-bottom: 4px;
  }
  /* back */
  .card-back { left: 520px; top: 560px; }
  .back-mark {
    position: absolute;
    left: -150px;
    top: 40px;
    width: 300px; height: 300px;
    border-radius: 50%;
    background: var(--red);
  }
  .back-brand {
    position: absolute;
    left: 175px;
    top: 300px;
    color: var(--ink);
    font-weight: 700;
    font-size: 15px;
    text-transform: uppercase;
    letter-spacing: 0.5px;
  }
  .contact {
    position: absolute;
    left: 290px;
    top: 90px;
  }
  .person {
    color: var(--grey);
    font-weight: 700;
    font-size: 30px;
    text-transform: uppercase;
    letter-spacing: 0.5px;
    margin-bottom: 16px;
  }
  .contact-list { list-style: none; }
  .contact-list li {
    display: flex;
    align-items: center;
    gap: 12px;
    color: var(--ink);
    font-weight: 500;
    font-size: 13px;
    margin-bottom: 10px;
  }
  .contact-list svg { width: 14px; height: 14px; flex: none; }
</style>
</head>
<body>

  <section class="card card-front" aria-label="Card front">
    <div class="brand">
      <div class="brand-dot"></div>
      <div class="brand-name">Brindlewood First Aid Training</div>
    </div>

    <div class="pitch">
      <p class="pitch-title">Onsite Training -</p>
      <p class="pitch-sub">We can come to you</p>
      <div class="pitch-rule"></div>
      <ul class="benefits">
        <li>Time efficient</li>
        <li>Cost effective</li>
        <li>Minimise downtime<br>for your team</li>
      </ul>
      <ul class="services">
        <li>First Aid Training</li>
        <li>WHS Training</li>
      </ul>
    </div>
  </section>

  <section class="card card-back" aria-label="Card back">
    <div class="back-mark"></div>
    <p class="back-brand">Brindlewood First Aid</p>

    <div class="contact">
      <h1 class="person">Daniel Harper</h1>
      <ul class="contact-list">
        <li>
          <svg viewBox="0 0 24 24" aria-hidden="true"><path fill="#ec1f24" d="M6.6 10.8a15.1 15.1 0 0 0 6.6 6.6l2.2-2.2a1 1 0 0 1 1-.25 11.4 11.4 0 0 0 3.6.57 1 1 0 0 1 1 1V20a1 1 0 0 1-1 1A17 17 0 0 1 3 4a1 1 0 0 1 1-1h3.5a1 1 0 0 1 1 1c0 1.25.2 2.45.57 3.57a1 1 0 0 1-.25 1z"/></svg>
          0400 318 562
        </li>
        <li>
          <svg viewBox="0 0 24 24" aria-hidden="true"><rect x="2" y="5" width="20" height="14" fill="#ec1f24"/><path d="M2 5l10 8 10-8" fill="none" stroke="#fff" stroke-width="1.6"/></svg>
          help@brindlewoodfirstaid.com.au
        </li>
        <li>
          <svg viewBox="0 0 24 24" aria-hidden="true"><g fill="none" stroke="#ec1f24" stroke-width="1.6"><circle cx="12" cy="12" r="9"/><ellipse cx="12" cy="12" rx="4" ry="9"/><path d="M3 12h18M5 7h14M5 17h14"/></g></svg>
          brindlewoodfirstaid.com.au
        </li>
      </ul>
    </div>
  </section>

</body>
</html>
```